Delivery Docket urgent plus require many other designs for more stationary after this.

We need a new delivery docket design urgently as the one we have needs updating and we have changed our company name. Please do not copy the one I have uploaded as we do not feel this looks professional enough. I uploaded it as a few designers requested to see what we are currently using thank you.
It is quite complex in that we need a range of information to be on the one docket.
We are a Transport Company based in Australia that has a wide variety of items that we deliver such as water, sand and gravels and heavy equipment transport.
We would prefer to keep this design to A5 size as we will get them made into books. We are looking for a modern professional look. Although it is only a delivery docket this is given to all our customers so needs to look impressive.

We need our new logo on the docket (PRW). There will also need to be areas for our address and contact numbers, email etc these will be supplied to the winning designer to make the final adjustments so for now just put something generic in these spaces.
Needs to have an area for customer details, purchase order number, date and docket number (docket number to be in red)
Needs a section where we can list the type of product / and or service that has been provided and the amount / qty usually 3 lines will be enough for this. Need area under this where the customer can sign name and print name to say that the goods / and or services have been received.

Also required somewhere on the docket are the words, Tax Invoice will be issued based on the information provided on this docket. Conditions on back of page

We then need a separate section on the same page which we will use internally that the staff member can tear off and hand into the office. On this section it needs to have area where the driver can list km at start of job and at end with space to calculate km travelled, details of fuel purchased eg amount and litres, vehicle that is being used. also need to log down wheel bearing temps.
prime mover needs spaces as follows
Steer axel FL____________ Steer axel FR _________ 1st drive axel L_______
1st drive axel R_________ 2nd drive axel L_______ 2nd drive axel R________

For the trailers need something similar x 2 as have 2 trailers
1st axel DS_________ 1st axel PS_________ 2nd axel DS__________
2nd axel PS_________ 3rd axel DS_________ 3rd axel PS__________

I have included a few examples of designs we have used in past and ones that we like so you can get an idea of the colours we prefer, I have included some of the designs we are currently receiving for our logo that I like so you can get idea again of colours we prefer. There is much more we need designed also such as time sheets, more delivery dockets and letter heads so there is a lot of more work available to the winning designer.

Thank you

Target Market(s)

Customers

Font styles to use
Serif
Sans Serif

Colors

Designer to choose colors to be used in the design.

Requirements
Should not have
• Please don't copy old docket as we do not like it and nned new info on new design thank you

```html
<!DOCTYPE html>
<html lang="en">
<head>
<meta charset="utf-8">
<title>PRW Delivery Docket</title>
<link rel="stylesheet" href="https://fonts.googleapis.com/css2?family=Montserrat:wght@400;500;600;700;800&display=swap">
<style>
  :root {
    --blue: #4a6cc2;
    --blue-deep: #3b58b0;
    --blue-band: rgba(52, 90, 210, 0.88);
    --charcoal: #363b48;
    --slate: #525867;
    --line: #8a8f99;
    --grid: #9aa0aa;
    --cell: #f1f2f4;
    --ink: #2b2f38;
    --haze: #eceef1;
    --red: #e0141b;
    --white: #ffffff;
  }
  * { box-sizing: border-box; margin: 0; padding: 0; }
  html, body { width: 1200px; height: 848px; overflow: hidden; background: var(--white); }
  body { font-family: "Montserrat", sans-serif; color: var(--ink); }
  .docket { position: relative; width: 1200px; height: 848px; overflow: hidden; background: var(--white); }
  .abs { position: absolute; }
  .decor { position: absolute; inset: 0; }

  .customer-head {
    left: 539px; top: 43px; width: 632px; height: 38px; background: var(--blue);
    color: var(--white); font-weight: 700; font-size: 19px;
    display: flex; align-items: center; justify-content: space-between; padding: 0 18px 0 16px;
  }
  .customer-head .docket-no { color: var(--red); }
  .customer-rows { left: 539px; top: 81px; width: 356px; border-left: 1px solid var(--line); border-right: 1px solid var(--line); }
  .customer-rows div {
    height: 31.5px; border-bottom: 1px solid var(--line);
    font-size: 13px; font-weight: 500; letter-spacing: -0.5px; padding: 10px 0 0 5px; color: var(--white);
  }
  .customer-rows div:first-child { color: var(--white); }

  .brand {
    left: 72px; top: 104px; font-weight: 800; font-size: 84px; line-height: 1;
    color: #e4e6ec; letter-spacing: 2px;
  }

  .items { left: 36px; top: 207px; width: 1135px; border-collapse: collapse; }
  .items th {
    background: var(--blue); color: var(--white); font-size: 20px; font-weight: 700;
    height: 31px; padding: 0;
  }
  .items td { height: 59px; background: var(--cell); border: 1.5px solid var(--grid); }
  .items .total td {
    background: var(--charcoal); border: none; height: 44px; color: var(--white);
    font-weight: 700; font-size: 21px; text-align: left; padding-left: 0;
  }

  .tax-note { left: 40px; top: 472px; font-size: 14.5px; font-weight: 500; line-height: 1.25; }
  .sign-line { left: 884px; top: 495px; width: 284px; border-top: 1.5px solid var(--line); }
  .sign-label { left: 884px; top: 506px; width: 252px; text-align: right; font-size: 19px; font-weight: 600; }

  .trip { left: 31px; top: 534px; width: 1135px; border-collapse: collapse; table-layout: fixed; }
  .trip th { background: var(--blue); color: var(--white); font-size: 19px; font-weight: 600; height: 32px; padding: 0; }
  .trip td { height: 61px; border: 1.5px solid var(--grid); background: var(--white); }

  .bearings { left: 31px; top: 641px; width: 1135px; height: 183px; border: 1.5px solid var(--grid); }
  .bearings .title {
    height: 29px; background: var(--charcoal); color: var(--white);
    font-size: 17px; font-weight: 600; text-align: center; line-height: 29px;
  }
  .bearings .sub { display: flex; height: 26px; margin-top: 2px; }
  .bearings .sub div {
    flex: 1; background: var(--slate); color: var(--white); text-align: center;
    font-size: 17px; font-weight: 600; line-height: 26px;
  }
  .bearings .sub div:first-child { flex: 0 0 562px; border-right: 2px solid var(--white); }
  .bearings .split { position: absolute; left: 562px; top: 57px; bottom: 0; border-left: 2px solid var(--charcoal); }

  .field { position: absolute; font-size: 16px; font-weight: 500; white-space: nowrap; }
  .rule { position: absolute; height: 0; border-top: 1.5px solid var(--ink); }
</style>
</head>
<body>
<main class="docket">
  <svg class="decor" width="1200" height="848" aria-hidden="true">
    <polygon points="585,0 700,0 530,260 415,260" fill="var(--haze)"/>
    <polygon points="820,0 1200,0 1200,120 742,120" fill="var(--haze)"/>
    <polygon points="1010,0 1200,0 1200,40 985,40" fill="#e2e4e8"/>
    <polygon points="1120,700 1200,700 1200,848 1020,848" fill="var(--haze)"/>
    <polygon points="85,95 781,95 712,204 10,204" fill="var(--blue-deep)"/>
  </svg>

  <div class="abs brand">PRW</div>

  <header class="abs customer-head">
    <span>Customer Details</span>
    <span>Delivery Docket <span class="docket-no">2050</span></span>
  </header>
  <div class="abs customer-rows">
    <div>Name:</div>
    <div>Order no:</div>
    <div>Contact:</div>
    <div>Billing Address:</div>
  </div>

  <table class="abs items">
    <colgroup><col style="width:178px"><col style="width:658px"><col style="width:299px"></colgroup>
    <tr><th>Qty</th><th>Description</th><th>Price</th></tr>
    <tr><td></td><td></td><td></td></tr>
    <tr><td></td><td></td><td></td></tr>
    <tr><td></td><td></td><td></td></tr>
    <tr class="total"><td></td><td></td><td>TOTAL</td></tr>
  </table>

  <p class="abs tax-note">Tax Invoice which will be issued based on the information<br>provided on this docket as well as the conditions on back of page.</p>
  <div class="abs sign-line"></div>
  <div class="abs sign-label">Customer Signature</div>

  <table class="abs trip">
    <colgroup>
      <col style="width:161px"><col style="width:190px"><col style="width:197px">
      <col style="width:188px"><col style="width:192px"><col style="width:207px">
    </colgroup>
    <tr><th>KM/start</th><th>KM/end</th><th>Distance</th><th>Fuel/price</th><th>Fuel/ltrs</th><th>Vehicle Type</th></tr>
    <tr><td></td><td></td><td></td><td></td><td></td><td></td></tr>
  </table>

  <section class="abs bearings">
    <div class="title">Wheel Bearing Temps</div>
    <div class="sub"><div>Prime Movers</div><div>Trailers</div></div>
    <div class="split"></div>
  </section>

  <svg class="decor" width="1200" height="848" aria-hidden="true">
    <polygon points="57,738 777,738 708,848 0,848 0,820" fill="var(--blue-band)"/>
  </svg>

  <span class="field" style="left:46px;top:706px">Steer Axel FL</span>
  <div class="rule" style="left:160px;top:720px;width:132px"></div>
  <span class="field" style="left:306px;top:706px">Steer Axel FR</span>
  <div class="rule" style="left:445px;top:720px;width:122px"></div>

  <span class="field" style="left:46px;top:748px">1st Drive Axel L</span>
  <div class="rule" style="left:160px;top:762px;width:132px"></div>
  <span class="field" style="left:306px;top:746px">1st Drive Axel R</span>
  <div class="rule" style="left:445px;top:760px;width:122px"></div>

  <span class="field" style="left:46px;top:791px">2nd Drive Axel L</span>
  <div class="rule" style="left:160px;top:805px;width:132px"></div>
  <span class="field" style="left:306px;top:789px">2nd Drive Axel R</span>
  <div class="rule" style="left:445px;top:803px;width:122px"></div>

  <span class="field" style="left:620px;top:708px">1st Axel DS</span>
  <div class="rule" style="left:741px;top:722px;width:121px"></div>
  <span class="field" style="left:916px;top:706px">1st Axel PS</span>
  <div class="rule" style="left:1019px;top:720px;width:121px"></div>

  <span class="field" style="left:620px;top:748px">2nd Axel DS</span>
  <div class="rule" style="left:741px;top:762px;width:121px"></div>
  <span class="field" style="left:907px;top:746px">2nd Axel PS</span>
  <div class="rule" style="left:1019px;top:760px;width:121px"></div>

  <span class="field" style="left:620px;top:790px">3rd Axel DS</span>
  <div class="rule" style="left:741px;top:804px;width:121px"></div>
  <span class="field" style="left:910px;top:788px">3rd Axel PS</span>
  <div class="rule" style="left:1019px;top:802px;width:121px"></div>
</main>
</body>
</html>
```